Snowplowing Flyer - 8.5x11, one sided

We are looking to redesign our flyer for winter snowplowing to match our other collateral material. I have attached a few files to show what our new marketing material looks like and we are looking to have a new flyer done that is: (1) 8.5"x11" (one sided); (2) CMYK for printing; and (3) minimum 300 dpi suitable for printing.

We would like color photo(s) of snowplowing trucks (at least one) and it should have the following text on it...

Our logo and contact information (just street/email/web/phone number)

Plowing whenever 1" of accumulated snow has fallen, normally by 6am depending upon time and amount

Plowing multiple times per 24 hour period during heavy snowfalls

A fleet of 20 plow trucks w multiple backup plow trucks to ensure our performance

Email based plowing information with real time updates for clients

Double driveways starting at $238, triple driveways starting at $258

Hand shoveling of front walkways and porches available

Salting of driveways available

Fully licensed and insured for your protection

Please contact us by phone or email to request a proposal.

Target Market(s)

Residential homeowners.

Industry/Entity Type

Snow Removal

Font styles to use
Sans Serif

Colors

Designer to choose colors to be used in the design.

Requirements
Must have
• A similar feel to the rest of our marketing material which I have attached. Should be easy to read and fun to look at.
Nice to have
• A photo of a snowplow truck similar to the one in our existing material and on our website.
Should not have
• Should not be cluttered. Should keep a similar color scheme to the rest of our marketing material.

```html
<!DOCTYPE html>
<html lang="en">
<head>
<meta charset="utf-8">
<title>Snowplowing Flyer</title>
<link href="https://fonts.googleapis.com/css2?family=Lato:wght@400;700;900&display=swap" rel="stylesheet">
<style>
  :root {
    --stage: #1b1e21;
    --ink: #0d0d0d;
    --green: #2fbf55;
    --blue: #5b9bd8;
    --white: #ffffff;
    --rule: #8a8a8a;
    --snow-light: #eef0f1;
    --snow-mid: #b9bec2;
  }
  * { box-sizing: border-box; margin: 0; padding: 0; }
  html, body { width: 1200px; height: 848px; overflow: hidden; }
  body { background: var(--stage); font-family: 'Lato', sans-serif; }
  .flyer {
    position: absolute; left: 290px; top: 23px;
    width: 620px; height: 802px; background: var(--ink); overflow: hidden;
  }
  .flyer-bg { position: absolute; inset: 0; }
  .logo-panel {
    position: absolute; left: 388px; top: 128px; width: 212px; height: 104px;
    background: var(--ink); border: 2px solid var(--green);
    color: var(--white); text-align: center; padding-top: 16px;
  }
  .logo-name { font-size: 21px; font-weight: 400; letter-spacing: 4px; }
  .logo-sub { font-size: 8px; letter-spacing: 5px; margin-top: 2px; color: var(--snow-mid); }
  .logo-phone { font-size: 17px; font-weight: 700; margin-top: 12px; letter-spacing: 1px; }
  .headline {
    position: absolute; left: 20px; top: 292px; width: 580px;
    color: var(--green); font-weight: 900; font-size: 23px; line-height: 1.18; text-align: center;
  }
  .service-list { position: absolute; left: 28px; top: 392px; width: 310px; list-style: none; color: var(--white); }
  .service-group { border-bottom: 1px solid var(--rule); padding: 8px 0; }
  .service-group:last-child { border-bottom: none; }
  .service-item { position: relative; padding-left: 14px; font-size: 12.5px; line-height: 1.25; margin: 2px 0; }
  .service-item::before {
    content: ""; position: absolute; left: 0; top: 4px;
    border-left: 7px solid var(--green); border-top: 4px solid transparent; border-bottom: 4px solid transparent;
  }
  .photo-grid {
    position: absolute; left: 350px; top: 400px; width: 246px; height: 246px;
    display: grid; grid-template-columns: 1fr 1fr; gap: 8px;
  }
  .photo-tile { border: 5px solid var(--white); }
  .tile-truck { background: linear-gradient(160deg, #f3f4f5, #9ea4a8 60%, #e6e8ea); }
  .tile-loader { background: linear-gradient(150deg, #ececec, #c98a3a 55%, #d9d9d9); }
  .tile-shovel { background: linear-gradient(140deg, #b59a82, #e8e6e4 55%, #c9313a); }
  .tile-spreader { background: linear-gradient(160deg, #7a7e80, #b79a7c 60%, #e2e3e4); }
  .contact-lead {
    position: absolute; left: 70px; top: 698px; width: 508px; line-height: 18px;
    color: var(--white); font-size: 14px; font-weight: 700; text-align: center;
  }
  .contact-details { position: absolute; left: 92px; top: 736px; color: var(--white); font-size: 14px; line-height: 24px; }
  .contact-line { display: flex; align-items: center; gap: 8px; }
  .contact-line svg { flex: none; }
</style>
</head>
<body>
  <main class="flyer">
    <svg class="flyer-bg" width="620" height="802" viewBox="0 0 620 802">
      <defs>
        <linearGradient id="snowScene" x1="0" y1="0" x2="1" y2="1">
          <stop offset="0" stop-color="#d9dcde"/>
          <stop offset="0.5" stop-color="#f2f3f4"/>
          <stop offset="1" stop-color="#c3c7ca"/>
        </linearGradient>
      </defs>
      <rect width="620" height="380" fill="url(#snowScene)" role="img" aria-label="Photo of a white pickup truck with a red snowplow clearing a snowy road"/>
      <path d="M0,110 C170,200 330,205 460,250 S600,330 620,345" fill="none" stroke="var(--blue)" stroke-width="7"/>
      <path d="M0,122 C170,212 330,217 460,262 S600,342 620,357 L620,802 L0,802 Z" fill="var(--ink)"/>
      <path d="M0,707 H70 M70,690 H560 Q578,690 578,707 Q578,724 560,724 H88 Q70,724 70,707 Q70,690 88,690 M578,707 H585 Q605,707 605,727 V802" fill="none" stroke="var(--green)" stroke-width="2.5"/>
    </svg>

    <div class="logo-panel">
      <div class="logo-name">BIRCH HOLLOW</div>
      <div class="logo-sub">LANDSCAPING</div>
      <div class="logo-phone">Ph: (555) 204-7719</div>
    </div>

    <h1 class="headline">Plowing Whenever 1" Of Accumulated<br>Snow Has Fallen, Normally By 6am Depending<br>Upon Time And Amount</h1>

    <ul class="service-list">
      <li class="service-group">
        <p class="service-item">Plowing multiple times per 24 hour period during heavy snowfalls</p>
      </li>
      <li class="service-group">
        <p class="service-item">A fleet of 20 plow trucks w multiple backup plow trucks to ensure our performance</p>
        <p class="service-item">Email based plowing information with real time updates for clients</p>
      </li>
      <li class="service-group">
        <p class="service-item">Double driveways starting at $238, triple driveways starting at $258</p>
      </li>
      <li class="service-group">
        <p class="service-item">Hand shoveling of front walkways and porches available</p>
        <p class="service-item">Salting of driveways available</p>
        <p class="service-item">Fully licensed and insured for your protection</p>
      </li>
    </ul>

    <div class="photo-grid">
      <div class="photo-tile tile-truck" role="img" aria-label="Photo of a plow truck pushing snow"></div>
      <div class="photo-tile tile-shovel" role="img" aria-label="Photo of a red shovel clearing snow from a walkway"></div>
      <div class="photo-tile tile-loader" role="img" aria-label="Photo of a loader moving snow"></div>
      <div class="photo-tile tile-spreader" role="img" aria-label="Photo of a truck spreading salt on a road"></div>
    </div>

    <p class="contact-lead">Please contact us by phone or email to request a proposal.</p>
    <div class="contact-details">
      <p class="contact-line">
        <svg width="14" height="14" viewBox="0 0 14 14"><circle cx="7" cy="7" r="6" fill="none" stroke="#fff" stroke-width="1.3"/><path d="M7 3.5a2.2 2.2 0 0 1 2.2 2.2C9.2 7.5 7 10.5 7 10.5S4.8 7.5 4.8 5.7A2.2 2.2 0 0 1 7 3.5Z" fill="#fff"/></svg>
        1480 Alder Ridge Road, Maple Falls, MI 49000
      </p>
      <p class="contact-line">
        <svg width="14" height="14" viewBox="0 0 14 14"><circle cx="7" cy="7" r="6" fill="none" stroke="#fff" stroke-width="1.3"/><path d="M4.6 3.8l1.3-.3.8 1.8-.9.7a4.5 4.5 0 0 0 2 2l.7-.9 1.8.8-.3 1.3c-3 .3-5.7-2.4-5.4-5.4Z" fill="#fff"/></svg>
        (555) 204-7719
        <svg width="14" height="14" viewBox="0 0 14 14"><circle cx="7" cy="7" r="6" fill="none" stroke="#fff" stroke-width="1.3"/><rect x="3.8" y="4.8" width="6.4" height="4.4" fill="#fff"/><path d="M3.8 4.8 7 7.3l3.2-2.5" fill="none" stroke="#0d0d0d" stroke-width="0.8"/></svg>
        hello@birchhollow.com
      </p>
    </div>
  </main>
</body>
</html>
```